I need to design a business card
on the front side the words "VELTRIS CAPITAL" with the top half surrounded by a stylised cloud. Minimalist, navy blue font on white background, with the Veltris capital in embossing.

On the back contact details (avoid centered). I would rather have the details taking the 2/3rd on the right and having the logo on the left, but anyway not plain centered

Marcello Lo Ruffo
CEO e Fondatore

m.loruffo@veltris-capital.example
+39.328.514.6082

Piazza Ventrano 7
20135 Milano

```html
<!DOCTYPE html>
<html lang="it">
<head>
<meta charset="utf-8">
<title>Veltris Capital – Biglietto da visita</title>
<link rel="stylesheet" href="https://fonts.googleapis.com/css2?family=Tinos:wght@400;700&family=Lato:wght@400&display=swap">
<style>
  :root {
    --navy: #022660;
    --ink: #1b1b1b;
    --paper: #ffffff;
    --stage: #1c1c1c;
    --rule: #2a2a2a;
  }
  * { margin: 0; padding: 0; box-sizing: border-box; }
  html, body { width: 1200px; height: 1059px; overflow: hidden; }
  body { background: var(--stage); position: relative; }

  .card {
    position: absolute;
    border-radius: 24px;
    overflow: hidden;
  }
  .card--front { left: 255px; top: 86px; width: 702px; height: 401px; background: var(--paper); }
  .card--back { left: 254px; top: 547px; width: 711px; height: 405px; background: var(--navy); }

  .brand-name {
    position: absolute;
    font-family: "Tinos", "Times New Roman", serif;
    font-weight: 700;
    line-height: 1;
    white-space: nowrap;
  }
  .card--front .brand-name { right: 36px; top: 164px; font-size: 26px; color: var(--navy); }
  .card--back .brand-name { left: 0; right: 0; top: 180px; text-align: center; font-size: 46px; color: var(--paper); }

  .holder { position: absolute; left: 37px; top: 232px; font-family: "Tinos", "Times New Roman", serif; }
  .holder__name { font-size: 27px; font-weight: 700; color: var(--navy); line-height: 1.2; }
  .holder__role { font-size: 17.5px; color: var(--ink); margin-top: 2px; }

  .divider { position: absolute; left: 37px; top: 309px; width: 632px; height: 1.5px; background: var(--rule); }

  .contacts { position: absolute; left: 37px; top: 322px; list-style: none; font-family: "Lato", Arial, sans-serif; font-size: 18px; color: var(--ink); }
  .contacts__item { display: flex; align-items: center; height: 34px; }
  .contacts__icon { width: 20px; height: 20px; margin-right: 12px; fill: var(--navy); }

  .address { position: absolute; right: 43px; top: 322px; font-family: "Lato", Arial, sans-serif; font-size: 18px; line-height: 24px; text-align: right; color: var(--ink); font-style: normal; }
</style>
</head>
<body>
  <section class="card card--front" aria-label="Fronte del biglietto">
    <p class="brand-name">VELTRIS CAPITAL</p>

    <div class="holder">
      <p class="holder__name">Marcello Lo Ruffo</p>
      <p class="holder__role">CEO e Fondatore</p>
    </div>

    <div class="divider"></div>

    <ul class="contacts">
      <li class="contacts__item">
        <svg class="contacts__icon" viewBox="0 0 24 24" aria-hidden="true"><path d="M6.6 10.8a15.1 15.1 0 0 0 6.6 6.6l2.2-2.2a1 1 0 0 1 1-.25 11.4 11.4 0 0 0 3.6.57 1 1 0 0 1 1 1V20a1 1 0 0 1-1 1A17 17 0 0 1 3 4a1 1 0 0 1 1-1h3.5a1 1 0 0 1 1 1c0 1.25.2 2.45.57 3.57a1 1 0 0 1-.25 1z"/></svg>
        <span>+39.328.514.6082</span>
      </li>
      <li class="contacts__item">
        <svg class="contacts__icon" viewBox="0 0 24 24" aria-hidden="true"><circle cx="12" cy="12" r="9.5" fill="none" stroke="var(--navy)" stroke-width="2"/><path d="M8 6c2 1 1 3 3 4s1 3-1 4-1 3-1 4c-2-1-4-3-4.5-6S6 6 8 6zM15 8c2 0 3 2 3 4s-2 3-3 2 0-3-1-4 0-2 1-2z"/></svg>
        <span>m.loruffo@veltris-capital.example</span>
      </li>
    </ul>

    <address class="address">Piazza Ventrano 7<br>20135 Milano</address>
  </section>

  <section class="card card--back" aria-label="Retro del biglietto">
    <p class="brand-name">VELTRIS CAPITAL</p>
  </section>
</body>
</html>
```